cover for CD- Single.

This design is for a CD cover. The design is at your disposal, using all of your creative talents.
Things to improve the photo: Cleaning the face, removing blemishes.
Design in black and white would be an option (Color would be another option). I reiterate it is up to your taste and criteria, any reform and art on the cover of Cd.
Name of the single: El Camino del Alba Serena
Artist Name: Marisol Quenteva

Target Market(s)

Single Music

Industry/Entity Type

Music

Colors

Designer to choose colors to be used in the design.

Requirements
Must have
• style, elegance, professionalism, spontaneity
Nice to have
• I want it to be as professional as possible.
Should not have
• Spelling errors.

```html
<!DOCTYPE html>
<html lang="es">
<head>
<meta charset="utf-8">
<title>El Camino del Alba Serena — Marisol Quenteva</title>
<link rel="stylesheet" href="https://fonts.googleapis.com/css2?family=Great+Vibes&family=Cormorant+Garamond:wght@500&display=swap">
<style>
  :root {
    --stage: #f1f1f1;
    --backdrop-light: #eeeeee;
    --backdrop-mid: #d6d6d6;
    --backdrop-soft: #c4c4c4;
    --photo-light: #e6e6e6;
    --photo-mid: #9a9a9a;
    --photo-dark: #2a2a2a;
    --photo-deep: #141414;
    --type-light: #f7f7f7;
    --type-dark: #1c1c1c;
  }
  * { margin: 0; padding: 0; box-sizing: border-box; }
  html, body {
    width: 1200px;
    height: 1000px;
    overflow: hidden;
    background: var(--stage);
  }
  .presentation {
    position: relative;
    width: 1200px;
    height: 1000px;
    overflow: hidden;
  }
  .backdrop-photo {
    position: absolute;
    left: 0; top: 0;
    width: 1200px;
    height: 712px;
    background:
      radial-gradient(ellipse 30% 40% at 20% 15%, var(--backdrop-soft) 0%, transparent 70%),
      radial-gradient(ellipse 25% 45% at 92% 30%, var(--backdrop-soft) 0%, transparent 75%),
      radial-gradient(ellipse 35% 30% at 55% 55%, var(--backdrop-mid) 0%, transparent 70%),
      linear-gradient(180deg, #dedede 0%, var(--backdrop-light) 100%);
  }
  .backdrop-floor {
    position: absolute;
    left: 0; top: 712px;
    width: 1200px;
    height: 288px;
    background: linear-gradient(180deg, #f3f3f3 0%, #f7f7f7 100%);
  }

  /* Cover */
  .cover, .cover-reflection {
    position: absolute;
    left: 60px;
    width: 633px;
    height: 633px;
    overflow: hidden;
  }
  .cover { top: 185px; box-shadow: 0 0 40px rgba(0,0,0,0.08); }
  .cover-photo {
    position: absolute;
    inset: 0;
    background:
      radial-gradient(ellipse 55% 60% at 35% 45%, var(--photo-light) 0%, #c9c9c9 45%, transparent 75%),
      radial-gradient(ellipse 40% 70% at 92% 30%, var(--photo-deep) 0%, transparent 80%),
      linear-gradient(100deg, #d2d2d2 0%, var(--photo-mid) 48%, var(--photo-dark) 75%, var(--photo-deep) 100%);
  }
  .cover-title {
    position: absolute;
    top: 36px;
    right: 14px;
    width: 220px;
    font-family: "Great Vibes", cursive;
    font-weight: 400;
    font-size: 44px;
    line-height: 0.9;
    color: var(--type-light);
    text-align: center;
  }
  .cover-title span, .panel-title span { display: block; }
  .cover-artist {
    position: absolute;
    left: 0; right: 0;
    bottom: 14px;
    font-family: "Cormorant Garamond", serif;
    font-weight: 500;
    font-size: 27px;
    letter-spacing: 0.14em;
    text-transform: uppercase;
    text-align: center;
    color: var(--type-light);
  }

  /* Reflection */
  .cover-reflection {
    top: 817px;
    height: 183px;
    opacity: 0.35;
  }
  .cover-reflection .mirror {
    position: absolute;
    left: 0; top: 0;
    width: 633px;
    height: 633px;
    transform: scaleY(-1);
    transform-origin: top;
    top: 633px;
  }
  .cover-reflection::after {
    content: "";
    position: absolute;
    inset: 0;
    background: linear-gradient(180deg, rgba(241,241,241,0.1) 0%, rgba(241,241,241,0.7) 100%);
  }

  /* Right panel */
  .title-panel {
    position: absolute;
    left: 790px;
    top: 220px;
    width: 310px;
    text-align: center;
  }
  .panel-title {
    font-family: "Great Vibes", cursive;
    font-weight: 400;
    font-size: 64px;
    line-height: 1.05;
    color: var(--type-dark);
  }
  .panel-artist {
    margin-top: 44px;
    font-family: "Cormorant Garamond", serif;
    font-weight: 500;
    font-size: 22px;
    letter-spacing: 0.17em;
    text-transform: uppercase;
    color: var(--type-dark);
  }
</style>
</head>
<body>
  <main class="presentation">
    <div class="backdrop-photo" role="img" aria-label="Soft blurred enlargement of the cover portrait in light greys"></div>
    <div class="backdrop-floor"></div>

    <section class="cover">
      <div class="cover-photo" role="img" aria-label="Black and white portrait of the singer with eyes closed, smiling softly, hand raised to her ear, dark hair to the right"></div>
      <h2 class="cover-title">
        <span>El Camino</span>
        <span>del Alba</span>
        <span>Serena</span>
      </h2>
      <p class="cover-artist">Marisol Quenteva</p>
    </section>

    <div class="cover-reflection" aria-hidden="true">
      <div class="mirror">
        <div class="cover-photo"></div>
        <p class="cover-artist">Marisol Quenteva</p>
      </div>
    </div>

    <section class="title-panel">
      <h1 class="panel-title">
        <span>El Camino</span>
        <span>del Alba</span>
        <span>Serena</span>
      </h1>
      <p class="panel-artist">Marisol Quenteva</p>
    </section>
  </main>
</body>
</html>
```